Dorian's Roam Almanac Mobile App

We need a sleek new design for our new mobile app we are launching in the South Pacific. This app will be released for both iPhone and Android. The app has already been developed and your new design will give it the finishing touch we need to release it to our audience. This will be the premiere tourism app for the South Pacific and will be advertised heavily in our successful print publications which are distributed internationally. We are looking for you to provide two designs (for two screens in our mobile app) for this competition. The selected winner will have the opportunity to design the remaining screens in our app and website as a separate contract.

Attached you will see a few of the screens that currently exist in our mobile app to give you a feel for the functionality. The two screens we want you to design for this competition are the main listing page and the category selection page. These two screens will be included in the uploaded files and will be clearly marked so you know what we are looking for.

Please feel free to reach out to us with any questions if you need any guidance in directing your designs. Show us something sleek, engaging, and ultimately something that will drive our users to want to engage with the businesses that are listed in the app.

Please see the uploaded files for a couple of our current designs, the two screens we want you to design for this competition, and a few samples of design ideas we like.

Best of Luck!

Target Market(s)

Travelers to the South Pacific

Industry/Entity Type

Travel Industry

Font styles to use
Serif
Sans Serif

Colors
0492cd
33a6d7
ec1f27
f04a50
85cae6
cee9f5
f59296
cedeed
fbd4d5

Requirements
Must have
• Clean, attractive design for the two screens mentioned in the brief.
Nice to have
• Icon sets, color guide, font selection
Should not have
• Project should not be too busy or incorporate too many different colors, styles, fonts, etc.

```html
<!DOCTYPE html>
<html lang="en">
<head>
<meta charset="utf-8">
<title>Dorian's Roam Almanac – Category Selection</title>
<link href="https://fonts.googleapis.com/css2?family=Montserrat:wght@400;500;700;800&display=swap" rel="stylesheet">
<style>
  :root {
    --stage: #e8e5e2;
    --screen: #ffffff;
    --ink: #1c1c24;
    --muted: #8c8c94;
    --rule: #e2e2e6;
    --blue: #33a6d7;
    --blue-deep: #0492cd;
    --red: #ec1f27;
    --orange: #f7941d;
    --sea-light: #85cae6;
    --sea-deep: #0a8a9c;
  }
  * { box-sizing: border-box; margin: 0; padding: 0; }
  html, body { width: 1200px; height: 1200px; overflow: hidden; }
  body {
    background: var(--stage);
    font-family: "Montserrat", Arial, sans-serif;
    color: var(--ink);
    position: relative;
  }
  .app-screen {
    position: absolute; left: 300px; top: 20px;
    width: 600px; height: 1160px;
    background: var(--screen);
    overflow: hidden;
    border-radius: 8px;
    box-shadow: 0 20px 60px rgba(0,0,0,.12);
  }
  .status-bar {
    position: absolute; top: 0; left: 0; right: 0; height: 44px;
    display: flex; align-items: center; justify-content: space-between;
    padding: 0 20px; font-size: 19px; font-weight: 500;
  }
  .status-bar .carrier { display: flex; align-items: center; gap: 8px; }
  .status-bar .battery { display: flex; align-items: center; gap: 8px; }
  .battery-cell { width: 40px; height: 18px; border: 2px solid var(--ink); border-radius: 3px; padding: 2px; position: relative; }
  .battery-cell::before { content: ""; display: block; width: 100%; height: 100%; background: var(--ink); border-radius: 1px; }
  .battery-cell::after { content: ""; position: absolute; right: -5px; top: 4px; width: 3px; height: 6px; background: var(--ink); border-radius: 0 2px 2px 0; }

  .header { position: absolute; top: 62px; left: 36px; right: 36px; height: 110px; border-bottom: 1px solid var(--rule); }
  .header h1 { font-size: 52px; font-weight: 800; letter-spacing: -0.5px; line-height: 1; }
  .location { margin-top: 14px; display: flex; align-items: center; gap: 8px; font-size: 24px; font-weight: 700; color: var(--muted); }
  .change-btn {
    position: absolute; right: 0; top: 36px;
    background: var(--red); color: #fff; font-size: 22px; font-weight: 600;
    border-radius: 30px; padding: 14px 30px;
  }

  .hero {
    position: absolute; top: 192px; left: 0; width: 600px; height: 330px;
    background: linear-gradient(120deg, var(--sea-deep) 0%, #1fb3be 40%, var(--sea-light) 65%, #eef6f5 85%);
  }
  .pager {
    position: absolute; left: 50%; bottom: 22px; transform: translateX(-50%);
    background: rgba(255,255,255,.45); border-radius: 16px; padding: 8px 14px;
    display: flex; gap: 12px;
  }
  .pager span { width: 10px; height: 10px; border-radius: 50%; background: rgba(40,60,70,.35); }
  .pager span.active { background: var(--ink); }

  .category { position: absolute; left: 0; width: 600px; height: 250px; }
  .category .icon { position: absolute; left: 36px; top: 10px; width: 100px; height: 90px; }
  .category h2 { position: absolute; left: 36px; top: 118px; font-size: 30px; font-weight: 800; }
  .category p { position: absolute; left: 36px; top: 162px; font-size: 17px; color: var(--muted); }
  .category .divider { position: absolute; left: 36px; width: 300px; top: 205px; height: 1px; background: var(--rule); }
  .category .accent-block { position: absolute; right: 0; top: 20px; width: 190px; height: 230px; }
  .category .photo {
    position: absolute; right: 40px; top: 45px; width: 240px; height: 190px;
    border: 8px solid #fff; box-shadow: 0 10px 26px rgba(0,0,0,.18);
  }
  .accommodation { top: 540px; }
  .accommodation .accent-block { background: var(--blue); }
  .accommodation .photo { background: linear-gradient(135deg, #cfe0ea 0%, #f2f4f5 50%, #b9c7cf 100%); }
  .transportation { top: 790px; }
  .transportation .accent-block { background: var(--red); }
  .transportation .photo { background: linear-gradient(180deg, #dfe3e6 0%, #dfe3e6 45%, #d6282e 60%, #b81a20 80%, #55585c 100%); }
  .dining { top: 1040px; }
  .dining .accent-block { background: var(--orange); }
  .dining .photo { background: linear-gradient(135deg, #fbc64a 0%, #f6b233 60%, #f0f0ec 100%); }
</style>
</head>
<body>
  <main class="app-screen">
    <div class="status-bar">
      <div class="carrier">
        <span>●●●●●</span><span>Meridian</span>
        <svg width="22" height="16" viewBox="0 0 22 16" aria-hidden="true"><path d="M1 5a15 15 0 0 1 20 0M4.5 8.5a10 10 0 0 1 13 0M8 12a5 5 0 0 1 6 0" fill="none" stroke="#1c1c24" stroke-width="2" stroke-linecap="round"/><circle cx="11" cy="14.5" r="1.5" fill="#1c1c24"/></svg>
      </div>
      <div class="time">9:41 AM</div>
      <div class="battery"><span>100%</span><span class="battery-cell"></span></div>
    </div>

    <header class="header">
      <h1>Cook Island</h1>
      <div class="location">
        <svg width="16" height="22" viewBox="0 0 16 22" aria-hidden="true"><path d="M8 1a7 7 0 0 0-7 7c0 5 7 13 7 13s7-8 7-13a7 7 0 0 0-7-7z" fill="#ec1f27"/><circle cx="8" cy="8" r="2.6" fill="#fff"/></svg>
        <span>Rarotonga</span>
        <svg width="14" height="10" viewBox="0 0 14 10" aria-hidden="true"><path d="M1 1h12L7 9z" fill="#1c1c24"/></svg>
      </div>
      <span class="change-btn">Change</span>
    </header>

    <section class="hero" role="img" aria-label="Aerial photo of turquoise waves breaking on a sandy beach">
      <div class="pager"><span class="active"></span><span></span><span></span><span></span></div>
    </section>

    <article class="category accommodation">
      <svg class="icon" viewBox="0 0 100 90" fill="none" stroke="#33a6d7" stroke-width="3" stroke-linejoin="round" aria-hidden="true">
        <path d="M28 84V14l38-6v76M66 84V30l16 4v50M18 84h76"/>
        <path d="M36 22h6v6h-6zM50 20h6v6h-6zM36 36h6v6h-6zM50 34h6v6h-6zM36 50h6v6h-6zM50 48h6v6h-6zM42 84V68h10v16"/>
        <circle cx="22" cy="8" r="3"/><path d="M88 8l6 6M94 8l-6 6"/>
      </svg>
      <h2>Accommodation</h2>
      <p>sed do eiusmod tempor incidid...</p>
      <div class="divider"></div>
      <div class="accent-block"></div>
      <div class="photo" role="img" aria-label="Photo of a modern white hotel building against a pale sky"></div>
    </article>

    <article class="category transportation">
      <svg class="icon" viewBox="0 0 100 90" fill="none" stroke="#ec1f27" stroke-width="3" stroke-linejoin="round" stroke-linecap="round" aria-hidden="true">
        <path d="M14 60V46l8-18h44l8 18v14z"/>
        <path d="M26 30l-4 14h44l-4-14"/>
        <path d="M20 60v10h10V60M58 60v10h10V60"/>
        <circle cx="24" cy="52" r="3"/><circle cx="64" cy="52" r="3"/><path d="M36 54h16"/>
        <path d="M12 8v10M7 13h10"/><circle cx="88" cy="28" r="3"/>
      </svg>
      <h2>Transportation</h2>
      <p>sed do eiusmod tempor incidid...</p>
      <div class="divider"></div>
      <div class="accent-block"></div>
      <div class="photo" role="img" aria-label="Photo of a red classic sports car parked by a grey wall"></div>
    </article>

    <article class="category dining">
      <svg class="icon" viewBox="0 0 100 90" fill="none" stroke="#f7941d" stroke-width="3" stroke-linejoin="round" stroke-linecap="round" aria-hidden="true">
        <path d="M30 10v22a8 8 0 0 0 16 0V10M38 10v70M52 80V10c10 6 12 22 8 34h-8"/>
        <path d="M10 30l6 6M16 30l-6 6"/><circle cx="80" cy="30" r="3"/>
      </svg>
      <div class="accent-block"></div>
      <div class="photo" role="img" aria-label="Photo of a plated dish on a yellow table"></div>
    </article>
  </main>
</body>
</html>
```